Telecommunications/Power civil contractor needs business card design

Were a new telecommunications/power underground civil contractor that is looking for a new business card design. Our company colours are silver or grey and orange. Feel free to use the white background logo or the black background logo.

Target Market(s)

Local contractors, utility companies, private sector mining/energy companies, developers.

Industry/Entity Type

Telecommunications

Contact Information for Business Card

Each card will need the following info:
Persons name:
Title:
E-mail:
Phone number:
Shop Address:
Mailing Address:

Requirements
Must have
• Each card will need the following info:
• Persons name:
• Title:
• E-mail:
• Phone number:
• Shop Address:
• Mailing Address:

```html
<!DOCTYPE html>
<html lang="en">
<head>
<meta charset="utf-8">
<title>Ridge Run Contracting Inc – Business Card</title>
<link href="https://fonts.googleapis.com/css2?family=Arimo:wght@400;700&display=swap" rel="stylesheet">
<style>
  :root {
    --page: #e9e7e4;
    --card: #2a2a2c;
    --orange: #f15a22;
    --silver: #b9b9bb;
    --grey: #8e8e91;
    --light: #d9d9db;
  }
  html, body {
    margin: 0;
    width: 1200px;
    height: 864px;
    overflow: hidden;
    background: var(--page);
    font-family: "Arimo", Arial, sans-serif;
  }
  .sheet {
    width: 1200px;
    height: 864px;
    display: flex;
    flex-direction: column;
    align-items: center;
    justify-content: center;
    gap: 32px;
  }
  .card {
    position: relative;
    width: 680px;
    height: 388px;
    background: var(--card);
    border-radius: 4px;
    overflow: hidden;
    box-shadow: 0 6px 18px rgba(0,0,0,.25);
  }
  .card svg.bands {
    position: absolute;
    inset: 0;
  }
  .brand {
    position: absolute;
    display: flex;
    align-items: center;
    gap: 14px;
  }
  .brand-mark {
    width: 46px;
    height: 46px;
    border-radius: 50%;
    border: 4px solid var(--orange);
    box-sizing: border-box;
    flex: none;
  }
  .brand-name {
    color: var(--orange);
    font-weight: 700;
    text-transform: uppercase;
    line-height: 1.05;
    letter-spacing: .06em;
  }
  /* front */
  .card-front .brand {
    left: 0; right: 0; top: 52px;
    flex-direction: column;
    gap: 16px;
  }
  .card-front .brand-mark { width: 76px; height: 76px; border-width: 6px; }
  .card-front .brand-name { font-size: 28px; text-align: center; }
  /* back */
  .contact {
    position: absolute;
    left: 200px;
    top: 40px;
    color: var(--grey);
    font-size: 14px;
    line-height: 1.45;
  }
  .person-name { color: var(--light); font-size: 26px; margin: 0; font-weight: 400; }
  .person-title { color: var(--orange); font-size: 17px; margin: 0 0 14px; }
  .address { margin: 0 0 10px; }
  .lines { list-style: none; margin: 0; padding: 0; }
  .lines li { display: flex; align-items: center; gap: 8px; }
  .lines svg { width: 14px; height: 14px; flex: none; }
  .divider {
    position: absolute;
    left: 380px; top: 264px;
    width: 260px; height: 1px;
    background: linear-gradient(90deg, transparent, #555 40%, transparent);
  }
  .card-back .brand { right: 36px; bottom: 40px; }
  .card-back .brand-mark { width: 60px; height: 60px; border-width: 5px; }
  .card-back .brand-name { font-size: 22px; }
</style>
</head>
<body>
<main class="sheet">

  <section class="card card-front" aria-label="Card front">
    <svg class="bands" width="680" height="388" viewBox="0 0 680 388" aria-hidden="true">
      <path d="M0 340 Q 360 322 680 268 L680 388 L0 388 Z" fill="var(--orange)"/>
      <path d="M0 336 Q 360 318 680 264" fill="none" stroke="var(--silver)" stroke-width="5"/>
    </svg>
    <div class="brand">
      <span class="brand-mark"></span>
      <span class="brand-name">Ridge Run<br>Contracting Inc</span>
    </div>
  </section>

  <section class="card card-back" aria-label="Card back">
    <svg class="bands" width="680" height="388" viewBox="0 0 680 388" aria-hidden="true">
      <path d="M0 0 L70 0 Q 120 230 250 388 L0 388 Z" fill="var(--orange)"/>
      <path d="M74 0 Q 124 230 256 388" fill="none" stroke="var(--silver)" stroke-width="5"/>
    </svg>

    <div class="contact">
      <h1 class="person-name">Alan Mercer</h1>
      <p class="person-title">General Manager</p>
      <p class="address">Street Address, Suite 00<br>Statename 00000</p>
      <ul class="lines">
        <li>
          <svg viewBox="0 0 16 16" aria-hidden="true"><rect x="4" y="1" width="8" height="14" rx="1.5" fill="none" stroke="currentColor" stroke-width="1.5"/></svg>
          555 0142 7731
        </li>
        <li>
          <svg viewBox="0 0 16 16" aria-hidden="true"><path d="M3 2h3l1 4-2 1a8 8 0 0 0 4 4l1-2 4 1v3a1 1 0 0 1-1 1A12 12 0 0 1 2 3a1 1 0 0 1 1-1z" fill="currentColor"/></svg>
          555 0198 2460
        </li>
        <li>
          <svg viewBox="0 0 16 16" aria-hidden="true"><rect x="1.5" y="3.5" width="13" height="9" fill="none" stroke="currentColor" stroke-width="1.5"/><path d="M1.5 4 8 9l6.5-5" fill="none" stroke="currentColor" stroke-width="1.5"/></svg>
          info@ridgeruncontracting.com
        </li>
        <li>
          <svg viewBox="0 0 16 16" aria-hidden="true"><circle cx="8" cy="8" r="6.5" fill="none" stroke="currentColor" stroke-width="1.5"/><path d="M1.5 8h13M8 1.5c-3 3.5-3 9.5 0 13M8 1.5c3 3.5 3 9.5 0 13" fill="none" stroke="currentColor" stroke-width="1.2"/></svg>
          www.ridgeruncontracting.com
        </li>
      </ul>
    </div>

    <div class="divider"></div>

    <div class="brand">
      <span class="brand-mark"></span>
      <span class="brand-name">Ridge Run<br>Contracting Inc</span>
    </div>
  </section>

</main>
</body>
</html>
```